KRM

I just wrote a novel that I plan on marketing through my website. Please use my uploaded files to add on to your design... The name of the book is "Lanterns under the frost".

Industry/Entity Type

Marketing

Font styles to use
Serif
Sans Serif

Colors

Designer to choose colors to be used in the design.

```html
<!DOCTYPE html>
<html lang="en">
<head>
<meta charset="utf-8">
<title>Lanterns under the frost</title>
<link href="https://fonts.googleapis.com/css2?family=Anton&family=Fjalla+One&family=Open+Sans:wght@300;400;700&family=Roboto+Slab:wght@400&display=swap" rel="stylesheet">
<style>
:root{
  --navy:#211c6e;
  --black:#000;
  --red:#b3121b;
  --deep-red:#8b0a0a;
  --gray:#ebebeb;
  --ink:#444;
  --muted:#666;
  --yellow:#ffd200;
  --white:#fff;
}
*{margin:0;padding:0;box-sizing:border-box}
html,body{width:1200px;height:1177px;overflow:hidden;background:var(--white)}
.page{position:relative;width:1200px;height:1177px;font-family:"Open Sans",Arial,sans-serif}
.abs{position:absolute}
.brand-mark{left:183px;top:22px;width:98px;height:98px;border-radius:50%;background:var(--black);color:var(--white);font-family:"Anton",sans-serif;font-size:30px;display:flex;align-items:center;justify-content:center}
.title{left:303px;top:40px;font-family:"Anton",sans-serif;font-size:58px;font-weight:400;line-height:1;white-space:nowrap;letter-spacing:4.4px}
.title .accent{color:var(--red)}
.title .rest{color:var(--black)}
.rule{left:0;top:137px;width:1200px;height:5px;background:var(--black)}
.nav{left:0;top:142px;width:1200px;height:47px;background:var(--navy);font-family:"Fjalla One",sans-serif;font-size:19px;color:var(--white)}
.nav a{position:absolute;top:2px;height:47px;line-height:47px;color:var(--white);text-decoration:none}
.nav .current{left:109px;top:0;width:125px;padding-top:2px;background:var(--black);text-align:center}
.hero{left:0;top:189px;width:1200px;height:338px;background:var(--black)}
.hero-band{left:0;top:527px;width:1200px;height:10px;background:var(--deep-red)}
.panel{position:absolute}
.panel-left{left:348px;top:189px;width:256px;height:303px;background:radial-gradient(ellipse at 45% 45%,#6b6a52 0%,#3e3e30 45%,#151512 100%)}
.panel-cash{left:607px;top:189px;width:233px;height:137px;background:radial-gradient(ellipse at 50% 50%,#d8d6c8 0%,#8f9080 45%,#1d1d1a 100%)}
.panel-group{left:607px;top:329px;width:233px;height:163px;background:linear-gradient(180deg,#2a2a2a 0%,#5a4a44 55%,#8a8580 100%)}
.panel-right{left:843px;top:189px;width:250px;height:303px;background:radial-gradient(ellipse at 45% 45%,#5a3a26 0%,#2e1d14 50%,#0a0706 100%)}
.book{left:136px;top:225px;width:212px;height:370px;background:var(--navy);box-shadow:4px 4px 8px rgba(0,0,0,.35);overflow:hidden}
.book-photo{position:absolute;left:0;top:0;width:212px;height:155px;background:linear-gradient(180deg,#9a8c7c 0%,#8a6b5a 50%,#6b7a55 100%)}
.book-stripe{position:absolute;left:0;top:155px;width:212px;height:5px;background:var(--red)}
.book-band{position:absolute;left:0;top:160px;width:212px;height:105px;background:linear-gradient(180deg,#2b2575 0%,#1b1640 70%,#3a1530 100%)}
.book-title{position:absolute;left:14px;top:200px;width:190px;font-family:"Roboto Slab",serif;font-size:11px;color:#e05050;transform:rotate(-6deg);white-space:nowrap}
.book-author{position:absolute;left:30px;top:318px;font-family:"Roboto Slab",serif;font-size:7px;letter-spacing:1px;color:#e05050;transform:rotate(-8deg);white-space:nowrap}
.price-frame{left:394px;top:492px;width:669px;height:100px;background:var(--white)}
.price{left:414px;top:510px;width:627px;height:73px;background:var(--black);color:var(--white);font-weight:300;font-size:36px;line-height:73px;text-align:right;padding-right:20px;white-space:nowrap;overflow:hidden}
.price .amount{font-size:40px}
.pitch{left:184px;top:626px;width:840px}
.pitch h2{font-family:Arial,Helvetica,sans-serif;font-weight:400;font-size:24px;color:var(--ink);line-height:1.1}
.pitch h2 span{color:var(--red)}
.pitch p{width:825px;font-family:Arial,Helvetica,sans-serif;font-size:13px;color:#333;line-height:17px;margin-top:1px}
.themes{left:0;top:742px;width:1200px;height:282px;background:var(--gray)}
.theme{position:absolute;top:56px;width:200px}
.theme .icon{display:block;width:78px;height:78px;margin:0 auto}
.theme h3{font-size:18px;font-weight:700;color:var(--ink);text-align:center;margin-top:12px;line-height:24px}
.theme p{width:210px;font-size:12.4px;color:var(--muted);line-height:15.6px;margin-top:4px}
.buy{left:0;top:1024px;width:1200px;height:114px;background:var(--navy)}
.buy h2{position:absolute;left:144px;top:20px;font-size:29px;font-weight:700;color:var(--yellow);white-space:nowrap;letter-spacing:-.3px}
.buy .or{position:absolute;left:146px;top:58px;font-size:30px;color:var(--yellow)}
.buy .links{position:absolute;left:211px;top:66px;font-family:Arial,sans-serif;font-size:12px;line-height:14px;color:var(--yellow)}
.buy .email{position:absolute;left:447px;top:66px;font-family:Arial,sans-serif;font-size:12px;color:var(--yellow)}
.call{position:absolute;left:745px;top:15px;width:318px;height:86px;background:var(--deep-red);color:var(--white);text-align:center}
.call .label{font-size:24px;line-height:28px;margin-top:8px;color:#f0f0f0}
.call .phone{font-size:41px;font-weight:700;line-height:48px;white-space:nowrap}
.legal{left:0;top:1138px;width:1200px;height:39px;background:var(--black);color:var(--white);font-family:Arial,sans-serif;font-size:14px;line-height:38px;text-align:center}
</style>
</head>
<body>
<div class="page">
  <header>
    <div class="abs brand-mark">KRM</div>
    <h1 class="abs title"><span class="accent">LANTERNS</span> <span class="rest">UNDER THE FROST</span></h1>
  </header>
  <div class="abs rule"></div>
  <nav class="abs nav">
    <a class="current" href="#">HOME</a>
    <a style="left:273px" href="#">ABOUT THE BOOK</a>
    <a style="left:463px" href="#">BOOK FEATURES</a>
    <a style="left:645px" href="#">AUTHOR</a>
    <a style="left:776px" href="#">CONTACT US</a>
  </nav>
  <section>
    <div class="abs hero"></div>
    <div class="abs hero-band"></div>
    <div class="panel panel-left" role="img" aria-label="Photo of a young man in an olive jacket looking down"></div>
    <div class="panel panel-cash" role="img" aria-label="Photo of hands counting banknotes"></div>
    <div class="panel panel-group" role="img" aria-label="Photo of a group of men posing in suits"></div>
    <div class="panel panel-right" role="img" aria-label="Photo of a man deep in thought against a dark background"></div>
    <div class="abs book">
      <div class="book-photo" role="img" aria-label="Cover photo of a man standing in a city street"></div>
      <div class="book-stripe"></div>
      <div class="book-band"></div>
      <div class="book-title">LANTERNS UNDER THE FROST</div>
      <div class="book-author">WRITTEN BY DESMOND R. VALE</div>
    </div>
    <div class="abs price-frame"></div>
    <div class="abs price">At <span class="amount">$14.99</span> you can own your copy.</div>
  </section>
  <section class="abs pitch">
    <h2>A story of <span>Money, Murder, Sex and family</span> ties in the heart of the city.</h2>
    <p>Ready along as Desmond R. Vale masterfully paint this Northgate Harbor tale like no other ~ The "M.O.B boys" clash in a rain of bullets against North sides own "Yayo boys."</p>
  </section>
  <section class="abs themes">
    <div class="theme" style="left:140px">
      <svg class="icon" viewBox="0 0 78 78"><circle cx="39" cy="39" r="39" fill="#222"/><circle cx="34" cy="44" r="10" fill="none" stroke="#fff" stroke-width="3"/><circle cx="46" cy="37" r="9" fill="#fff"/><text x="34" y="49" font-size="13" font-weight="700" fill="#fff" text-anchor="middle" font-family="Arial">$</text><text x="46" y="42" font-size="12" font-weight="700" fill="#222" text-anchor="middle" font-family="Arial">$</text></svg>
      <h3>money</h3>
      <p>Ut enim ad minim veniaxam, quis nostrud exercittion ullamco laboris nisi ut aliquip ex ea commodo consequat.</p>
    </div>
    <div class="theme" style="left:373px">
      <svg class="icon" viewBox="0 0 78 78"><circle cx="39" cy="39" r="39" fill="#222"/><circle cx="39" cy="39" r="13" fill="none" stroke="#fff" stroke-width="3"/><path d="M39 20v12M39 46v12M20 39h12M46 39h12" stroke="#fff" stroke-width="3"/></svg>
      <h3>murder</h3>
      <p>Duis aute irure dolor in reprehderit in volptate velit esse cillm dolore eu fugiat nulla paiatur. Excepteur sint occaecat cupidatatnon proident.</p>
    </div>
    <div class="theme" style="left:608px">
      <svg class="icon" viewBox="0 0 78 78"><circle cx="39" cy="39" r="39" fill="#222"/><circle cx="33" cy="36" r="9" fill="none" stroke="#fff" stroke-width="3.5"/><path d="M33 45v14M27 53h12" stroke="#fff" stroke-width="3.5"/><circle cx="44" cy="40" r="9" fill="none" stroke="#fff" stroke-width="3.5"/><path d="M50 34l8-8M51 26h7v7" stroke="#fff" stroke-width="3.5" fill="none"/></svg>
      <h3>sex</h3>
      <p>Ut enim ad minim veniaxam, quis nostrud exercittion ullamco laboris nisi ut aliquip ex ea commodo consequat.</p>
    </div>
    <div class="theme" style="left:846px">
      <svg class="icon" viewBox="0 0 78 78"><circle cx="39" cy="39" r="39" fill="#222"/><g fill="#fff"><circle cx="28" cy="32" r="4.5"/><circle cx="39" cy="30" r="5"/><circle cx="50" cy="32" r="4.5"/><path d="M21 48v-5a7 7 0 0 1 14 0v5z"/><path d="M31 48v-6a8 8 0 0 1 16 0v6z"/><path d="M43 48v-5a7 7 0 0 1 14 0v5z"/></g></svg>
      <h3>family</h3>
      <p>Duis aute irure dolor in reprehderit in volptate velit esse cillm dolore eu fugiat nulla paiatur. Excepteur sint occaecat cupidatatnon proident.</p>
    </div>
  </section>
  <footer>
    <div class="abs buy">
      <h2>TO PURCHASE YOUR ORDER BACK COPY</h2>
      <span class="or">or</span>
      <div class="links">www.krmpresshouse.com<br>www.lanternsunderthefrost.com</div>
      <div class="email">email: lanternsfrost24@mailbox.com</div>
      <div class="call">
        <div class="label">Contact Des Vale @</div>
        <div class="phone">555-014-2277</div>
      </div>
    </div>
    <div class="abs legal">We accept credit and debit cards for those individuals who wish to order on-line!</div>
  </footer>
</div>
</body>
</html>
```